Letterhead, stationery and email signature for construction business

I need the letterhead, stationery and email signature designs for a construction business. I want them to have a corporate feel to them.

I've attached the logo for reference.

```html
<!DOCTYPE html>
<html lang="en">
<head>
<meta charset="utf-8">
<title>Hartwell Build — Stationery</title>
<link href="https://fonts.googleapis.com/css2?family=Roboto:wght@400;500;700&display=swap" rel="stylesheet">
<style>
  :root{
    --blue:#2f56a6;
    --slate:#4b4e60;
    --ink:#3a3c44;
    --paper:#ffffff;
    --stage-top:#3a3c40;
    --stage:#57585b;
    --header-a:#f2f2f3;
    --header-b:#b9babd;
  }
  *{margin:0;padding:0;box-sizing:border-box}
  html,body{width:1200px;height:2464px;overflow:hidden}
  body{font-family:"Roboto",Arial,sans-serif;color:var(--ink);background:var(--stage);position:relative}
  .abs{position:absolute}
  .header{left:0;top:0;width:1200px;height:152px;background:linear-gradient(180deg,var(--header-b),var(--header-a) 45%,var(--header-b));}
  .cards-stage{left:0;top:152px;width:1200px;height:838px;background:var(--stage-top)}
  .paper{background:var(--paper);box-shadow:0 10px 24px rgba(0,0,0,.35)}
  .lockup{display:flex;align-items:center;gap:.35em;color:var(--blue);font-weight:700;letter-spacing:.02em;white-space:nowrap}
  .lockup .mark{width:1.1em;height:1.1em;background:var(--blue);flex:none}
  .contact{list-style:none;color:var(--ink)}
  .contact li{display:flex;align-items:flex-start;gap:6px;line-height:1.25}
  .contact svg{flex:none;fill:var(--blue)}
  .name{color:var(--blue);font-weight:700;letter-spacing:.01em}
  .role{color:var(--ink)}
  .block{background:var(--blue)}
  .block.slate{background:var(--slate)}
</style>
</head>
<body>
<svg width="0" height="0" style="position:absolute" aria-hidden="true">
  <symbol id="i-pin" viewBox="0 0 12 12"><rect width="12" height="12" rx="2"/><path d="M6 2.2a2.6 2.6 0 0 0-2.6 2.6C3.4 7 6 9.8 6 9.8S8.6 7 8.6 4.8A2.6 2.6 0 0 0 6 2.2zm0 3.6a1 1 0 1 1 0-2 1 1 0 0 1 0 2z" fill="#fff"/></symbol>
  <symbol id="i-phone" viewBox="0 0 12 12"><rect width="12" height="12" rx="2"/><path d="M4 2.5l1.2 1.8-.8.9a5 5 0 0 0 2.4 2.4l.9-.8 1.8 1.2-.6 1.3C6 9.3 2.7 6 2.7 3.1z" fill="#fff"/></symbol>
  <symbol id="i-mail" viewBox="0 0 12 12"><rect width="12" height="12" rx="2"/><rect x="2.4" y="3.4" width="7.2" height="5.2" fill="none" stroke="#fff" stroke-width=".9"/><path d="M2.6 3.6 6 6.4l3.4-2.8" fill="none" stroke="#fff" stroke-width=".9"/></symbol>
  <symbol id="i-web" viewBox="0 0 12 12"><rect width="12" height="12" rx="2"/><path d="M4 2.5v6.6l1.6-1.5 1.2 2.4 1-.5-1.2-2.3H8.8z" fill="#fff"/></symbol>
</svg>

<header class="abs header">
  <div class="abs lockup" style="left:392px;top:54px;font-size:40px">
    <span class="mark"></span>HARTWELL BUILD
  </div>
</header>

<section class="abs cards-stage" aria-label="Business cards">
  <article class="abs paper business-card-back" style="left:70px;top:190px;width:500px;height:290px">
    <div class="abs lockup" style="left:28px;top:28px;font-size:24px"><span class="mark"></span>HARTWELL BUILD</div>
    <ul class="abs contact" style="left:30px;top:104px;font-size:14px">
      <li style="margin-bottom:8px"><svg width="14" height="14"><use href="#i-pin"/></svg><span>78 Ridgeline Ave. Suite<br>210 Fort Worth, TX 0000</span></li>
      <li style="margin-bottom:6px"><svg width="14" height="14"><use href="#i-phone"/></svg>001-555-0188</li>
      <li style="margin-bottom:6px"><svg width="14" height="14"><use href="#i-mail"/></svg>info@hartwellbuild.com</li>
      <li><svg width="14" height="14"><use href="#i-web"/></svg>HartwellBuild.com</li>
    </ul>
    <div class="abs" style="right:28px;top:30px;text-align:right">
      <div class="name" style="font-size:24px">DANA ELLERY</div>
      <div class="role" style="font-size:12px;margin-top:2px">Chief Executive Officer</div>
    </div>
    <div class="abs block" style="right:40px;bottom:34px;width:96px;height:96px"></div>
  </article>

  <article class="abs paper business-card-front" style="left:630px;top:190px;width:500px;height:290px">
    <div class="abs block slate" style="left:0;top:0;width:150px;height:290px"></div>
    <div class="abs block" style="left:150px;top:0;width:120px;height:200px"></div>
    <div class="abs lockup" style="left:196px;top:222px;font-size:26px"><span class="mark"></span>HARTWELL BUILD</div>
  </article>
</section>

<section aria-label="Stationery set">
  <article class="abs app-screen" style="left:90px;top:1125px;width:330px;height:470px;background:radial-gradient(circle at 50% 45%,#ffffff,#c9cacd)">
    <div class="abs block" style="left:95px;top:150px;width:140px;height:150px"></div>
  </article>

  <article class="abs paper letterhead" style="left:505px;top:1040px;width:472px;height:665px">
    <div class="abs lockup" style="left:20px;top:22px;font-size:18px"><span class="mark"></span>HARTWELL BUILD</div>
    <ul class="abs contact" style="right:18px;top:24px;font-size:8.5px;text-align:right">
      <li><span>78 Ridgeline Ave. Suite<br>210 Fort Worth, TX 0000</span><svg width="11" height="11"><use href="#i-pin"/></svg></li>
    </ul>
    <div class="abs block" style="left:0;bottom:14px;width:52px;height:58px"></div>
    <ul class="abs contact" style="left:58px;bottom:16px;font-size:8.5px">
      <li style="margin-bottom:4px"><svg width="10" height="10"><use href="#i-phone"/></svg>001-555-0188</li>
      <li style="margin-bottom:4px"><svg width="10" height="10"><use href="#i-mail"/></svg>info@hartwellbuild.com</li>
      <li><svg width="10" height="10"><use href="#i-web"/></svg>HartwellBuild.com</li>
    </ul>
  </article>

  <article class="abs paper mini-card-front" style="left:858px;top:1131px;width:230px;height:142px">
    <div class="abs block slate" style="left:0;top:0;width:70px;height:142px"></div>
    <div class="abs block" style="left:70px;top:16px;width:46px;height:126px"></div>
    <div class="abs lockup" style="left:122px;top:92px;font-size:11px"><span class="mark"></span>HARTWELL BUILD</div>
  </article>

  <article class="abs paper mini-card-back" style="left:858px;top:1327px;width:232px;height:142px">
    <div class="abs lockup" style="left:16px;top:18px;font-size:11px"><span class="mark"></span>HARTWELL BUILD</div>
    <div class="abs" style="right:12px;top:18px;text-align:right">
      <div class="name" style="font-size:11px">DANA ELLERY</div>
      <div class="role" style="font-size:5.5px">Chief Executive Officer</div>
    </div>
    <ul class="abs contact" style="left:16px;top:70px;font-size:6.5px">
      <li style="margin-bottom:5px"><svg width="7" height="7"><use href="#i-pin"/></svg><span>78 Ridgeline Ave. Suite<br>210 Fort Worth, TX 0000</span></li>
      <li style="margin-bottom:3px"><svg width="7" height="7"><use href="#i-phone"/></svg>001-555-0188</li>
      <li style="margin-bottom:3px"><svg width="7" height="7"><use href="#i-mail"/></svg>info@hartwellbuild.com</li>
      <li><svg width="7" height="7"><use href="#i-web"/></svg>HartwellBuild.com</li>
    </ul>
    <div class="abs block" style="right:18px;bottom:16px;width:44px;height:50px"></div>
  </article>

  <article class="abs paper email-signature" style="left:63px;top:1757px;width:624px;height:158px">
    <div class="abs lockup" style="left:22px;top:18px;font-size:22px"><span class="mark"></span>HARTWELL BUILD</div>
    <div class="abs" style="left:22px;top:70px">
      <div class="name" style="font-size:17px">DANA ELLERY</div>
      <div class="role" style="font-size:7.5px;margin-top:1px">Chief Executive Officer</div>
    </div>
    <ul class="abs contact" style="left:22px;top:108px;font-size:8.5px">
      <li style="margin-bottom:4px"><svg width="10" height="10"><use href="#i-phone"/></svg>001-555-0188</li>
      <li style="margin-bottom:4px"><svg width="10" height="10"><use href="#i-mail"/></svg>info@hartwellbuild.com</li>
      <li><svg width="10" height="10"><use href="#i-web"/></svg>HartwellBuild.com</li>
    </ul>
    <ul class="abs contact" style="left:156px;top:108px;font-size:8.5px">
      <li><svg width="10" height="10"><use href="#i-pin"/></svg><span>78 Ridgeline Ave. Suite<br>210 Fort Worth, TX 0000</span></li>
    </ul>
    <div class="abs block" style="right:22px;bottom:18px;width:52px;height:58px"></div>
  </article>

  <article class="abs paper envelope" style="left:466px;top:1981px;width:674px;height:337px">
    <div class="abs lockup" style="left:22px;top:26px;font-size:24px"><span class="mark"></span>HARTWELL BUILD</div>
    <ul class="abs contact" style="left:22px;bottom:16px;font-size:8.5px">
      <li><svg width="10" height="10"><use href="#i-pin"/></svg>78 Ridgeline Ave. Suite 210 Fort Worth, TX 0000</li>
    </ul>
    <div class="abs block" style="right:24px;bottom:20px;width:54px;height:60px"></div>
  </article>
</section>
</body>
</html>
```